Varnel Solutions requires a new business card.

We are an online professional tool store.

Target Market(s)

We target the professional technician.

Industry/Entity Type

Business

Contact Information for Business Card

VarnelSolutions.com.au

sales@varnelsolutions.com

Requirements
Must have
• Needs to look commercial and professional
Should not have
• No Australian Colors, maps or shapes.
• No Shapes of Tools

```html
<!DOCTYPE html>
<html lang="en">
<head>
<meta charset="utf-8">
<title>Varnel Solutions – Business Card</title>
<link href="https://fonts.googleapis.com/css2?family=Lato:wght@400;700&display=swap" rel="stylesheet">
<style>
  :root {
    --stage: #3a3a3a;
    --brand-blue: #1528c4;
    --brand-teal: #1c98cf;
    --paper: #ffffff;
    --ink-light: #ffffff;
  }
  * { margin: 0; padding: 0; box-sizing: border-box; }
  html, body { width: 1200px; height: 900px; overflow: hidden; }
  body {
    background: var(--stage);
    font-family: "Lato", sans-serif;
    display: flex;
    align-items: center;
    justify-content: center;
    gap: 60px;
  }
  .card {
    position: relative;
    width: 525px;
    height: 300px;
    overflow: hidden;
    box-shadow: 0 14px 34px rgba(0,0,0,.45);
  }
  .card-front { background: var(--paper); }
  .card-back {
    background: var(--brand-blue);
    display: flex;
    flex-direction: column;
    align-items: center;
    justify-content: center;
    gap: 22px;
  }
  .front-shape { position: absolute; inset: 0; width: 100%; height: 100%; z-index: 0; }
  .wordmark {
    font-weight: 700;
    font-size: 34px;
    letter-spacing: .5px;
    line-height: 1;
  }
  .card-front .wordmark {
    position: absolute;
    z-index: 1;
    top: 40px;
    left: 40px;
    color: var(--brand-blue);
  }
  .card-back .wordmark { color: var(--ink-light); font-size: 40px; }
  .back-url { color: var(--ink-light); font-size: 15px; letter-spacing: .5px; }
  .address {
    position: absolute;
    z-index: 1;
    left: 30px;
    top: 168px;
    color: var(--ink-light);
    font-style: normal;
    font-size: 14px;
    line-height: 1.4;
  }
  .contact {
    position: absolute;
    z-index: 1;
    right: 26px;
    bottom: 16px;
    text-align: right;
    color: var(--ink-light);
  }
  .contact-name { color: var(--brand-teal); font-size: 23px; line-height: 1.1; }
  .contact-role { font-size: 14px; margin-bottom: 6px; }
  .contact-list { list-style: none; font-size: 13px; line-height: 1.4; }
  .contact-list li { display: flex; align-items: center; justify-content: flex-end; gap: 8px; }
  .contact-icon { width: 12px; height: 12px; flex: none; }
</style>
</head>
<body>
  <section class="card card-front" aria-label="Business card front">
    <svg class="front-shape" viewBox="0 0 525 300" preserveAspectRatio="none" aria-hidden="true">
      <path d="M0,112 C150,182 360,172 525,78 L525,300 L0,300 Z" fill="var(--brand-blue)"/>
      <path d="M140,156 C260,176 400,160 525,86" fill="none" stroke="var(--brand-teal)" stroke-width="4"/>
    </svg>
    <div class="wordmark">Varnel Solutions</div>
    <address class="address">418 Harlow Street<br>Austin, TX 78704</address>
    <div class="contact">
      <p class="contact-name">Dalton Kessler</p>
      <p class="contact-role">Manager</p>
      <ul class="contact-list">
        <li>512 555 0142
          <svg class="contact-icon" viewBox="0 0 12 12"><path d="M2 1 L4.5 1 L5.5 3.5 L4 4.5 C4.8 6.3 5.7 7.2 7.5 8 L8.5 6.5 L11 7.5 L11 10 C6 10.5 1.5 6 2 1 Z" fill="var(--brand-teal)"/></svg>
        </li>
        <li>512 555 0143
          <svg class="contact-icon" viewBox="0 0 12 12"><rect x="3" y="1" width="6" height="3" fill="var(--brand-teal)"/><rect x="1" y="4.5" width="10" height="5" rx="1" fill="var(--brand-teal)"/><rect x="3" y="8" width="6" height="3" fill="var(--ink-light)" stroke="var(--brand-teal)"/></svg>
        </li>
        <li>sales@varnelsolutions.com
          <svg class="contact-icon" viewBox="0 0 12 12"><rect x="1" y="2.5" width="10" height="7" fill="var(--brand-teal)"/><path d="M1 2.5 L6 6.5 L11 2.5" fill="none" stroke="var(--brand-blue)" stroke-width="1"/></svg>
        </li>
        <li>www.varnelsolutions.com.au
          <svg class="contact-icon" viewBox="0 0 12 12"><circle cx="6" cy="6" r="5" fill="var(--brand-teal)"/><path d="M1 6 H11 M6 1 C3.5 3.5 3.5 8.5 6 11 M6 1 C8.5 3.5 8.5 8.5 6 11" fill="none" stroke="var(--brand-blue)" stroke-width=".8"/></svg>
        </li>
      </ul>
    </div>
  </section>

  <section class="card card-back" aria-label="Business card back">
    <div class="wordmark">Varnel Solutions</div>
    <p class="back-url">www.varnelsolutions.com.au</p>
  </section>
</body>
</html>
```